Copper Hollow Sparkling

Hi all,

Thanks for taking the time to check out our brief.

Copper Hollow is an Australian wine company based in Victoria, and have been around for more than 20 years. We have a well-known sparkling Chardonnay Pinot Noir that needs a package revamp and we need your help!

Check out our current package here: http://www.copperhollowvino.com.au/our-wines/dsp-default_b.cfm?loadref=17

So here's the brief:

1. Use of the Copper Hollow logo (silhouette) and text mandatory - but can be as small/large as required.

2. Design must be shown on a sparkling bottle.

3. Can be closed with cork or crown seal - neck label/hood not mandatory.

4. Front label size to be no larger than 75mm high x 100mm wide. Back label to be no larger than 75mm x 100mm

5. Label does not have to be square/rectangular. Happy to see thoughts outside the box.

6. Design cannot be printed onto the bottle - must be on a label that can be applied to the bottle.

7. Be forward thinking. Be interesting. This design does not have to tie into our still (red and white) wine range.

8. Mandatory information to be shown on front label - a. Wine of Australia - b. Sparkling Chardonnay Pinot Noir

9. Mandatory info for front label - a. 750mL - b. Alcohol e.g. 13.5% ALC/VOL - c. Wine of Australi - d. Producer address (please insert dummy address at this stage - e. standard drinks e.g. approx 8.0 standard drinks (this can also be shown in the standard drinks glass logo) - f. space for a tasting blurb

10. Try to stay away from anything floral or overly girly.

Industry/Entity Type

Floral

Requirements
Must have
• Design must be shown on a sparkling wine bottle & include the full label design separately
Should not have
• Try to stay away from anything too floral and overly girly.

```html
<!DOCTYPE html>
<html lang="en">
<head>
<meta charset="utf-8">
<title>Copper Hollow Sparkling – Front Label</title>
<link rel="stylesheet" href="https://fonts.googleapis.com/css2?family=Marcellus&family=Source+Sans+3:ital,wght@0,400;0,700;1,400&display=swap">
<style>
  :root {
    --paper: #ffffff;
    --ink: #231f20;
    --frame: #1e1e1e;
    --orange-light: #f9c88a;
    --orange-mid: #f39a3c;
    --orange-deep: #ee6a2f;
  }
  html, body {
    margin: 0;
    padding: 0;
    width: 1200px;
    height: 1000px;
    overflow: hidden;
    background: var(--paper);
  }
  .canvas {
    position: relative;
    width: 1200px;
    height: 1000px;
  }
  .label {
    position: absolute;
    left: 221px;
    top: 215px;
    width: 758px;
    height: 569px;
    box-sizing: border-box;
    border: 5px solid var(--frame);
    background: var(--paper);
    color: var(--ink);
    overflow: hidden;
  }
  .label__splash {
    position: absolute;
    left: 126px;
    top: 22px;
    width: 627px;
    height: 441px;
  }
  .label__brand {
    position: absolute;
    left: 31px;
    top: 14px;
    margin: 0;
    font-family: "Marcellus", serif;
    font-weight: 400;
    font-size: 48px;
    letter-spacing: 0.36em;
    line-height: 1;
    white-space: nowrap;
  }
  .label__origin {
    position: absolute;
    right: 36px;
    top: 80px;
    margin: 0;
    font-family: "Source Sans 3", sans-serif;
    font-weight: 700;
    font-size: 23px;
    letter-spacing: 0.08em;
    line-height: 1;
  }
  .label__mark {
    position: absolute;
    left: 393px;
    top: 180px;
    width: 230px;
    display: flex;
    align-items: center;
    justify-content: center;
    gap: 10px;
    font-family: "Source Sans 3", sans-serif;
    font-weight: 700;
    font-size: 22px;
    letter-spacing: 0.06em;
    color: var(--ink);
    white-space: nowrap;
  }
  .label__mark-dot {
    width: 14px;
    height: 14px;
    border-radius: 50%;
    background: var(--ink);
  }
  .label__variety {
    position: absolute;
    left: 31px;
    top: 486px;
    margin: 0;
    font-family: "Source Sans 3", sans-serif;
    font-style: italic;
    font-size: 23px;
    line-height: 1;
  }
  .label__producer {
    position: absolute;
    left: 31px;
    top: 522px;
    margin: 0;
    font-family: "Source Sans 3", sans-serif;
    font-style: italic;
    font-size: 15px;
    line-height: 1;
  }
  .label__volume {
    position: absolute;
    right: 58px;
    top: 486px;
    margin: 0;
    font-family: "Source Sans 3", sans-serif;
    font-style: italic;
    font-size: 23px;
    line-height: 1;
  }
  .label__alcohol {
    position: absolute;
    right: 58px;
    top: 522px;
    margin: 0;
    font-family: "Source Sans 3", sans-serif;
    font-style: italic;
    font-size: 15px;
    line-height: 1;
  }
</style>
</head>
<body>
<main class="canvas">
  <section class="label" aria-label="Copper Hollow sparkling front label">
    <svg class="label__splash" viewBox="0 0 627 441" role="img" aria-label="Orange watercolour paint splash illustration">
      <defs>
        <radialGradient id="splash-tone" cx="60%" cy="45%" r="60%">
          <stop offset="0%" stop-color="var(--orange-deep)"/>
          <stop offset="55%" stop-color="var(--orange-mid)"/>
          <stop offset="100%" stop-color="var(--orange-light)"/>
        </radialGradient>
      </defs>
      <path fill="url(#splash-tone)" d="M120 150 C150 110 220 120 260 90 C300 40 380 20 450 40 C520 60 560 110 600 160 C630 210 620 270 600 320 C580 380 520 420 460 410 C400 400 360 360 300 350 C240 345 190 330 150 300 C90 270 60 210 120 150 Z"/>
    </svg>

    <h1 class="label__brand">COPPER HOLLOW</h1>
    <p class="label__origin">WINE OF AUSTRALIA</p>

    <div class="label__mark">
      <span class="label__mark-dot" aria-hidden="true"></span>
      <span>Copper Hollow</span>
    </div>

    <p class="label__variety">Sparkling Chardonnay Pinot Noir</p>
    <p class="label__producer">Copper Hollow Inc 48 Cask Lane Bendigo, VIC, 3550</p>
    <p class="label__volume">750ml</p>
    <p class="label__alcohol">13.5% alc/vol</p>
  </section>
</main>
</body>
</html>
```